Bulk Food Container sticker

Our company sells bulk snacks to office locations. We re-package all sorts of foods into re-usable "Vessaline" type containers for consistency. We need to create a designed sticker which has room to laser-print the name of the food. The "blank" sticker needs to be designed with our logo, etc... I have attached 2 files. The first is an example from another company doing a similar work, and the second is the template from the company that will be printing the stickers for me. See our website for examples of our current corporate identity. www.brindlemoorbeans.com
Target Market(s)
Offices, tech companies
Industry/Entity Type
Printing
Look and feel

```html
<!DOCTYPE html>
<html lang="en">
<head>
<meta charset="utf-8">
<title>Brindlemoor Coffee Service – Container Sticker</title>
<link href="https://fonts.googleapis.com/css2?family=Archivo:wght@300;800&display=swap" rel="stylesheet">
<style>
  :root {
    --brown: #7a400d;
    --orange: #e5721f;
    --white: #ffffff;
    --page: #ffffff;
  }
  html, body {
    margin: 0;
    padding: 0;
    width: 1200px;
    height: 1184px;
    overflow: hidden;
    background: var(--page);
  }
  .canvas {
    position: relative;
    width: 1200px;
    height: 1184px;
  }
  .sticker {
    position: absolute;
    left: 57px;
    top: 46px;
    width: 1086px;
    height: 1074px;
    border-radius: 40px;
    background: var(--brown);
    overflow: hidden;
  }
  .sticker__stripes {
    position: absolute;
    inset: 0;
    width: 100%;
    height: 100%;
  }
  .sticker__stripes polygon { fill: var(--orange); }
  .brand {
    position: absolute;
    left: 0;
    right: 0;
    top: 92px;
    text-align: center;
    color: var(--white);
  }
  .brand__name {
    margin: 0;
    font-family: "Archivo", Arial, sans-serif;
    font-weight: 800;
    font-size: 142px;
    line-height: 1;
    letter-spacing: -2px;
  }
  .brand__tagline {
    position: absolute;
    right: 140px;
    top: 162px;
    margin: 0;
    font-family: "Archivo", Arial, sans-serif;
    font-weight: 300;
    font-size: 34px;
    letter-spacing: 7px;
    color: var(--white);
  }
  .label-area {
    position: absolute;
    left: 66px;
    top: 309px;
    width: 935px;
    height: 712px;
    border-radius: 24px;
    background: var(--white);
  }
</style>
</head>
<body>
  <div class="canvas">
    <div class="sticker">
      <svg class="sticker__stripes" viewBox="0 0 1086 1074" preserveAspectRatio="none" aria-hidden="true">
        <polygon points="448,0 628,0 1086,300 1086,470"/>
        <polygon points="800,0 965,0 1086,80 1086,190"/>
      </svg>
      <div class="brand">
        <h1 class="brand__name">Brindlemoor</h1>
        <p class="brand__tagline">COFFEE SERVICE</p>
      </div>
      <div class="label-area"></div>
    </div>
  </div>
</body>
</html>
```